Cool Website Design Bright Coat Studio.

We need a new website, using our existing domain, with a similar function to https://www.plomfilmworks.com/ or https://www.trexafoilcraft.com/ instagram bright_coat.studio.
We can send google docs with pictures.
Logo attached

```html
<!DOCTYPE html>
<html lang="en">
<head>
<meta charset="utf-8">
<title>Bright Coat Studio — Custom Vehicle Wraps</title>
<link href="https://fonts.googleapis.com/css2?family=Roboto:wght@300;400;500;700;900&family=Montserrat:ital,wght@0,400;0,600;1,400&display=swap" rel="stylesheet">
<style>
:root{
  --bg:#000;
  --text:#fff;
  --purple:#7b3fe4;
  --blue:#2189e6;
  --teal:#0b2a3b;
  --muted:#6d6d6d;
  --grad:linear-gradient(90deg,var(--purple),var(--blue));
}
*{margin:0;padding:0;box-sizing:border-box}
html,body{width:1200px;height:3605px;overflow:hidden;background:var(--bg);color:var(--text);font-family:"Roboto",sans-serif}
.page{position:relative;width:1200px;height:3605px;overflow:hidden}
.abs{position:absolute}
.tri{position:absolute;width:0;height:0}
.tri-left{border-top:122px solid transparent;border-bottom:122px solid transparent;border-left:142px solid var(--teal);left:0}
.tri-right{border-top:125px solid transparent;border-bottom:125px solid transparent;border-right:150px solid var(--teal);right:0}

.brand{font-family:"Roboto",sans-serif;font-weight:700;color:var(--purple);white-space:nowrap}
.brand-header{left:112px;top:34px;font-size:22px}
.brand-header::before{content:"";display:inline-block;width:14px;height:14px;background:var(--blue);margin-right:8px;vertical-align:-1px}

.nav{left:466px;top:50px;font-size:15px;font-weight:500}
.nav a{color:var(--text);text-decoration:none;position:absolute;white-space:nowrap}
.nav a.active{color:var(--blue)}
.phone-badge{left:847px;top:39px;width:72px;height:42px;background:var(--grad);clip-path:polygon(30% 0,100% 0,70% 100%,0 100%)}
.phone-badge svg{position:absolute;left:28px;top:13px}
.call{left:929px;top:38px;font-size:17px;font-weight:500;line-height:26px;white-space:nowrap}
.call strong{font-weight:700;display:block}

.hero-title{left:112px;top:188px;font-size:58px;font-weight:900;line-height:70px;letter-spacing:.5px;white-space:nowrap}
.hero-title .accent{color:var(--purple)}
.tagline{left:112px;top:411px;font-size:18px;font-weight:500}
.btn{display:flex;align-items:center;justify-content:center;color:var(--text);font-size:15px;font-weight:500;background:var(--grad);clip-path:polygon(12% 0,100% 0,88% 100%,0 100%);text-decoration:none}
.hero-btn{left:112px;top:469px;width:172px;height:42px}
.photo{position:absolute}
.hero-photo{left:648px;top:137px;width:469px;height:429px;background:linear-gradient(180deg,#5a86c8 0%,#8fb2d8 25%,#3a3f44 55%,#55555a 80%,#7b7566 100%)}

.mark{position:absolute;left:50%;width:56px;height:6px;margin-left:-28px;background:var(--grad);transform:skewX(-30deg)}
.section-title{position:absolute;left:0;width:1200px;text-align:center;font-size:40px;font-weight:300;letter-spacing:.5px}
.section-title b{font-weight:700;color:var(--blue)}

.svc{position:absolute;top:738px;width:237px;height:256px}
.svc .photo{left:0;top:0;width:100%;height:100%}
.svc.selected .photo{outline:3px solid var(--purple);outline-offset:-3px}
.svc-label{position:absolute;left:20px;bottom:-17px;width:197px;height:42px;display:flex;align-items:center;justify-content:center;font-size:17px;font-weight:700;background:var(--blue);clip-path:polygon(12% 0,100% 0,88% 100%,0 100%)}
.svc.selected .svc-label{background:var(--purple)}
.arrow{position:absolute;width:30px;height:30px;border-radius:50%;background:#fff}
.arrow svg{position:absolute;left:5px;top:5px}

.story-photo{left:112px;top:1186px;width:445px;height:521px;background:linear-gradient(180deg,#7a8a6d 0%,#b59a5c 25%,#2d2730 50%,#5a2f6a 70%,#6d6256 100%)}
.story-title{position:absolute;left:640px;top:1236px;font-size:40px;font-weight:300;white-space:nowrap}
.story-title b{font-weight:700;color:var(--blue)}
.story-text{position:absolute;left:641px;width:446px;font-size:15px;line-height:32.7px}
.story-btn{left:641px;top:1652px;width:171px;height:42px}

.gal{position:absolute}
.gal-btn{left:487px;top:2500px;width:224px;height:44px}

.review{position:absolute;top:2786px;width:300px;height:282px;border:3px solid var(--purple);font-family:"Montserrat",sans-serif;overflow:hidden}
.review.dim .r-name,.review.dim .r-date,.review.dim .r-text{opacity:.35}
.avatar{position:absolute;left:18px;top:14px;width:76px;height:76px;border-radius:50%;border:3px solid var(--blue);background:linear-gradient(180deg,#c9a98a,#7b6a5c)}
.r-name{position:absolute;left:106px;top:32px;font-size:17px;font-weight:600;text-transform:uppercase;white-space:nowrap}
.r-date{position:absolute;left:106px;top:58px;font-size:12.5px;white-space:nowrap}
.r-text{position:absolute;left:18px;top:112px;width:262px;font-size:11.4px;font-style:italic;line-height:24px;white-space:nowrap}

.foot-brand{left:170px;top:3282px;font-size:31px}
.foot-brand::before{content:"";display:inline-block;width:18px;height:18px;background:var(--blue);margin-right:10px;vertical-align:0}
.follow{left:157px;top:3414px;font-size:14px}
.social{position:absolute;top:3451px;width:20px;height:20px;border-radius:50%;border:2px solid #fff}
.foot-head{position:absolute;top:3264px;font-size:21px;font-weight:500;white-space:nowrap}
.foot-list{position:absolute;top:3316px;list-style:none;font-size:15px;line-height:26.2px;white-space:nowrap}
.rule{left:136px;top:3520px;width:978px;height:1px;background:#777}
.copy{left:0;top:3547px;width:1200px;text-align:center;font-size:15px}
</style>
</head>
<body>
<div class="page">

  <div class="tri tri-left" style="top:518px"></div>
  <div class="tri tri-right" style="top:1630px"></div>
  <div class="tri tri-left" style="top:2520px"></div>
  <div class="tri tri-right" style="top:3080px"></div>

  <header>
    <div class="abs brand brand-header">Bright Coat Studio</div>
    <nav class="abs nav">
      <a class="active" href="#" style="left:0">HOME</a>
      <a href="#" style="left:76px">ABOUT US</a>
      <a href="#" style="left:181px">SERVICES</a>
      <a href="#" style="left:283px">GALLERY</a>
    </nav>
    <div class="abs phone-badge">
      <svg width="16" height="16" viewBox="0 0 24 24"><path fill="#fff" d="M6.6 10.8a15 15 0 0 0 6.6 6.6l2.2-2.2c.3-.3.7-.4 1-.2 1.1.4 2.3.6 3.6.6.6 0 1 .4 1 1V20c0 .6-.4 1-1 1A17 17 0 0 1 3 4c0-.6.4-1 1-1h3.5c.6 0 1 .4 1 1 0 1.2.2 2.4.6 3.6.1.3 0 .7-.2 1z"/></svg>
    </div>
    <div class="abs call">Call Us<strong>+1 555-010-4400</strong></div>
  </header>

  <section class="hero">
    <h1 class="abs hero-title">CUSTOM VEHICLE<br><span class="accent">WRAPS &amp; VINYL</span><br>GRAPHICS</h1>
    <p class="abs tagline">Precision. Quality. Stand-out style</p>
    <a class="abs btn hero-btn" href="#">GET A QUOTE</a>
    <div class="photo hero-photo" role="img" aria-label="Photo of a matte grey wrapped electric sedan parked on grass"></div>
  </section>

  <section class="services">
    <div class="mark" style="top:624px"></div>
    <h2 class="section-title" style="top:658px">OUR <b>SERVICES</b></h2>
    <div class="svc" style="left:112px">
      <div class="photo" role="img" aria-label="Photo of a car with a full matte grey wrap" style="background:linear-gradient(180deg,#6e9bd0 0%,#4e5358 45%,#2f3236 100%)"></div>
      <div class="svc-label">Full Wraps</div>
    </div>
    <div class="svc selected" style="left:360px">
      <div class="photo" role="img" aria-label="Photo of a car with a partial pink wrap" style="background:linear-gradient(180deg,#7d8a6a 0%,#b7647f 55%,#6a6f6c 100%)"></div>
      <div class="svc-label">Partial Wraps</div>
    </div>
    <div class="svc" style="left:605px">
      <div class="photo" role="img" aria-label="Photo of a car with teal and black custom graphics" style="background:linear-gradient(180deg,#9fb0a0 0%,#3fd3d0 45%,#1f2a2c 100%)"></div>
      <div class="svc-label">Custom Graphics</div>
    </div>
    <div class="svc" style="left:853px">
      <div class="photo" role="img" aria-label="Photo of a black pickup truck with door decals" style="background:linear-gradient(180deg,#bfc4c8 0%,#2b2d30 50%,#9a9690 100%)"></div>
      <div class="svc-label">Decals</div>
    </div>
    <div class="arrow" style="left:95px;top:851px"><svg width="20" height="20" viewBox="0 0 20 20"><path d="M16 10H5M9 5l-5 5 5 5" stroke="#000" stroke-width="2.6" fill="none"/></svg></div>
    <div class="arrow" style="left:1074px;top:851px"><svg width="20" height="20" viewBox="0 0 20 20"><path d="M4 10h11M11 5l5 5-5 5" stroke="#000" stroke-width="2.6" fill="none"/></svg></div>
  </section>

  <section class="story">
    <div class="photo story-photo" role="img" aria-label="Photo of a pickup truck with a black and purple wrap in a field"></div>
    <div class="mark" style="top:1205px;left:672px"></div>
    <h2 class="story-title">OUR <b>STORY</b></h2>
    <p class="story-text" style="top:1308px">Sed ut perspiciatis unde omnis iste natus error sit voluptatem accusantium doloremque laudantium, totam rem aperiam, eaque ipsa quae ab illo inventore veritatis et quasi architecto beatae vitae dicta sunt explicabo. Nemo enim ipsam voluptatem quia voluptas sit aspernatur aut odit aut fugit, sed quia consequuntur magni dolores eos qui ratione voluptatem sequi nesciunt.</p>
    <p class="story-text" style="top:1521px">Sed ut perspiciatis unde omnis iste natus error sit voluptatem accusantium doloremque laudantium, totam rem aperiam, eaque ipsa quae ab illo inventore</p>
    <a class="abs btn story-btn" href="#">READ MORE</a>
  </section>

  <section class="gallery">
    <div class="mark" style="top:1841px"></div>
    <h2 class="section-title" style="top:1876px">WRAP <b>GALLERY</b></h2>
    <div class="photo gal" role="img" aria-label="Photo of a red sports car with black racing stripes" style="left:112px;top:1957px;width:307px;height:242px;background:linear-gradient(180deg,#b7b1a8 0%,#c62a2e 45%,#2a2a2c 60%,#b8232a 100%)"></div>
    <div class="photo gal" role="img" aria-label="Photo of a black wrapped luxury sedan in a garage" style="left:451px;top:1957px;width:308px;height:499px;background:linear-gradient(180deg,#6b5a50 0%,#9aa0a8 30%,#25262b 55%,#1c1d22 100%)"></div>
    <div class="photo gal" role="img" aria-label="Photo of a white trailer with lettered business graphics" style="left:780px;top:1957px;width:308px;height:242px;background:linear-gradient(180deg,#efede6 0%,#d9d6cf 70%,#5a5550 100%)"></div>
    <div class="photo gal" role="img" aria-label="Photo of a white sedan with tinted windows" style="left:112px;top:2213px;width:307px;height:243px;background:linear-gradient(180deg,#3a3632 0%,#e9e9eb 45%,#8a8682 100%)"></div>
    <div class="photo gal" role="img" aria-label="Photo of a black wrapped off-road vehicle" style="left:780px;top:2213px;width:308px;height:243px;background:linear-gradient(180deg,#c8cdd3 0%,#2b2c2e 50%,#8d8a84 100%)"></div>
    <a class="abs btn gal-btn" href="#">VIEW ALL GALLERY</a>
  </section>

  <section class="reviews">
    <div class="mark" style="top:2636px"></div>
    <h2 class="section-title" style="top:2671px">WHAT <b>CUSTOMERS SAY</b></h2>
    <article class="review dim" style="left:112px">
      <div class="avatar" role="img" aria-label="Customer portrait"></div>
      <div class="r-name">Ravi Tolan</div><div class="r-date">01 Oct 2025</div>
      <p class="r-text">Sed ut perspiciatis unde omnis iste<br>natus error sit voluptatem accusantium<br>doloremque laudantium, totam rem<br>aperiam, eaque ipsa quae ab illo<br>inventore veritatis et quasi architecto<br>beatae vitae dicta sunt explicabo.</p>
    </article>
    <article class="review" style="left:449px">
      <div class="avatar" role="img" aria-label="Customer portrait"></div>
      <div class="r-name">Ravi Tolan</div><div class="r-date">01 Oct 2025</div>
      <p class="r-text">Sed ut perspiciatis unde omnis iste<br>natus error sit voluptatem accusantium<br>doloremque laudantium, totam rem<br>aperiam, eaque ipsa quae ab illo<br>inventore veritatis et quasi architecto<br>beatae vitae dicta sunt explicabo.</p>
    </article>
    <article class="review dim" style="left:788px">
      <div class="avatar" role="img" aria-label="Customer portrait"></div>
      <div class="r-name">Ravi Tolan</div><div class="r-date">01 Oct 2025</div>
      <p class="r-text">Sed ut perspiciatis unde omnis iste<br>natus error sit voluptatem accusantium<br>doloremque laudantium, totam rem<br>aperiam, eaque ipsa quae ab illo<br>inventore veritatis et quasi architecto<br>beatae vitae dicta sunt explicabo.</p>
    </article>
    <div class="arrow" style="left:62px;top:2907px"><svg width="20" height="20" viewBox="0 0 20 20"><path d="M16 10H5M9 5l-5 5 5 5" stroke="#000" stroke-width="2.6" fill="none"/></svg></div>
    <div class="arrow" style="left:1108px;top:2907px"><svg width="20" height="20" viewBox="0 0 20 20"><path d="M4 10h11M11 5l5 5-5 5" stroke="#000" stroke-width="2.6" fill="none"/></svg></div>
  </section>

  <footer>
    <div class="abs brand foot-brand">Bright Coat Studio</div>
    <div class="abs follow">Follow us on socials</div>
    <span class="social" style="left:155px"></span>
    <span class="social" style="left:201px"></span>
    <span class="social" style="left:247px"></span>
    <span class="social" style="left:293px"></span>

    <h3 class="foot-head" style="left:571px">QUICK LINKS</h3>
    <ul class="foot-list" style="left:572px">
      <li>Shop</li><li>About</li><li>Contact</li><li>Returns</li><li>Privacy Policy</li><li>Terms</li>
    </ul>
    <h3 class="foot-head" style="left:854px">CUSTOMER SERVICE</h3>
    <ul class="foot-list" style="left:856px">
      <li>Vinyl Wraps</li><li>Stratashield Paint Protection Film</li><li>Matte Paint Protection Film</li><li>Coloured PPF</li><li>Ceramic Coating</li><li>Car Detailing</li><li>Custom Decals</li>
    </ul>
    <div class="abs rule"></div>
    <p class="abs copy">© 2025 Bright Coat Studio | All Rights Reserved.</p>
  </footer>

</div>
</body>
</html>
```